Business cards & stationary
QVM247: Tuition Debt Relief
Use same font as used in my logo
Use logo font in logo, but easier to read font for rest of card
Simple
Gavin Morrow
President & CEO
2918 Fernhollow Dr
Blacklick, OH 43871
1-855-7-QVM-247
gmorrow@QVM247.example
www.QVM247.example
Please see logo project.
TBD. For now, please have an image take up the back...part or all of logo. Or just the top part "QVM247.example"
logo in AI format
logo color info

```html
<!DOCTYPE html>
<html lang="en">
<head>
<meta charset="utf-8">
<title>QVM247 Stationery Set</title>
<link href="https://fonts.googleapis.com/css2?family=Russo+One&family=Open+Sans:wght@400;600;700&display=swap" rel="stylesheet">
<style>
  :root{
    --bg:#5b5c5e;
    --green:#17733a;
    --green-dark:#0e5628;
    --grey:#9a9c9e;
    --grey-light:#d9dadb;
    --white:#ffffff;
    --ink:#3a3a3a;
    --logo-font:"Russo One", sans-serif;
    --body-font:"Open Sans", sans-serif;
  }
  *{margin:0;padding:0;box-sizing:border-box}
  html,body{width:1200px;height:961px;overflow:hidden}
  body{background:var(--bg);font-family:var(--body-font);position:relative}
  .piece{position:absolute;overflow:hidden;box-shadow:0 6px 18px rgba(0,0,0,.35)}
  .wave{position:absolute;left:0;bottom:0;width:100%}
  .logo{font-family:var(--logo-font);font-weight:400;letter-spacing:1px;display:flex;align-items:center;gap:8px;line-height:1}
  .logo .mark{display:inline-block;background:currentColor}
  .logo--green{color:var(--green)}
  .logo--white{color:var(--white)}

  /* Folder */
  .folder{left:60px;top:60px;width:420px;height:560px;background:linear-gradient(160deg,var(--green),var(--green-dark))}
  .folder .logo{position:absolute;left:0;right:0;top:220px;justify-content:center;font-size:58px}
  .folder .logo .mark{width:14px;height:14px}
  .folder .tagline{position:absolute;left:0;right:0;top:296px;text-align:center;color:var(--white);font-size:18px;letter-spacing:4px}

  /* Letterhead */
  .letterhead{left:520px;top:60px;width:400px;height:560px;background:var(--white)}
  .letterhead .logo{position:absolute;left:28px;top:30px;font-size:26px}
  .letterhead .logo .mark{width:8px;height:8px}
  .letterhead .contact{position:absolute;right:26px;top:28px;font-size:7.5px;line-height:1.6;color:var(--ink);text-align:left}
  .letterhead .web{position:absolute;left:0;right:0;bottom:14px;text-align:center;font-size:7px;color:var(--white);z-index:2}

  /* CD */
  .disc{left:955px;top:120px;width:200px;height:200px;border-radius:50%;background:linear-gradient(150deg,var(--green),var(--green-dark))}
  .disc .hole{position:absolute;left:78px;top:78px;width:44px;height:44px;border-radius:50%;background:var(--bg);border:8px solid var(--grey-light)}
  .disc .logo{position:absolute;left:0;right:0;top:40px;justify-content:center;font-size:22px}
  .disc .logo .mark{width:6px;height:6px}

  /* Envelope */
  .envelope{left:60px;top:665px;width:440px;height:220px;background:var(--white)}
  .envelope .logo{position:absolute;left:22px;top:22px;font-size:24px}
  .envelope .logo .mark{width:7px;height:7px}
  .envelope .return{position:absolute;left:22px;top:54px;font-size:7.5px;line-height:1.6;color:var(--ink)}

  /* Business cards */
  .card{width:300px;height:172px}
  .card-front{left:540px;top:690px;background:var(--white)}
  .card-front .logo{position:absolute;left:20px;top:52px;font-size:26px}
  .card-front .logo .mark{width:8px;height:8px}
  .card-front .divider{position:absolute;left:150px;top:30px;width:1px;height:88px;background:var(--grey)}
  .card-front .details{position:absolute;left:162px;top:28px;font-size:7.5px;line-height:1.55;color:var(--ink)}
  .card-front .name{font-weight:700;font-size:10px;color:var(--green)}
  .card-front .role{font-weight:600;margin-bottom:4px}
  .card-back{left:870px;top:690px;background:linear-gradient(160deg,var(--green),var(--green-dark))}
  .card-back .logo{position:absolute;left:0;right:0;top:62px;justify-content:center;font-size:36px}
  .card-back .logo .mark{width:10px;height:10px}
  .card-back .web{position:absolute;left:0;right:0;bottom:18px;text-align:center;color:var(--white);font-size:8px;letter-spacing:1px}
</style>
</head>
<body>

  <section class="piece folder">
    <div class="logo logo--white">QVM247<span class="mark"></span></div>
    <p class="tagline">Know. Budget. Grow.</p>
    <svg class="wave" viewBox="0 0 420 70" height="70" preserveAspectRatio="none">
      <path d="M0 40 Q140 0 260 30 T420 20 V70 H0Z" fill="var(--grey)"/>
      <path d="M0 50 Q140 14 260 42 T420 32 V70 H0Z" fill="var(--green-dark)"/>
    </svg>
  </section>

  <section class="piece letterhead">
    <div class="logo logo--green">QVM247<span class="mark"></span></div>
    <div class="contact">
      2918 Fernhollow Dr<br>
      Blacklick, OH 43871<br>
      1-855-7-QVM-247<br>
      www.QVM247.example
    </div>
    <svg class="wave" viewBox="0 0 400 60" height="60" preserveAspectRatio="none">
      <path d="M0 22 Q130 -4 250 18 T400 8 V60 H0Z" fill="var(--grey-light)"/>
      <path d="M0 34 Q130 8 250 30 T400 20 V60 H0Z" fill="var(--green)"/>
    </svg>
    <p class="web">www.QVM247.example</p>
  </section>

  <section class="piece disc">
    <div class="logo logo--white">QVM247<span class="mark"></span></div>
    <div class="hole"></div>
  </section>

  <section class="piece envelope">
    <div class="logo logo--green">QVM247<span class="mark"></span></div>
    <div class="return">
      2918 Fernhollow Dr<br>
      Blacklick, OH 43871
    </div>
    <svg class="wave" viewBox="0 0 440 50" height="50" preserveAspectRatio="none">
      <path d="M0 20 Q150 -2 280 18 T440 8 V50 H0Z" fill="var(--grey-light)"/>
      <path d="M0 30 Q150 8 280 28 T440 18 V50 H0Z" fill="var(--green)"/>
    </svg>
  </section>

  <section class="piece card card-front">
    <div class="logo logo--green">QVM247<span class="mark"></span></div>
    <div class="divider"></div>
    <div class="details">
      <p class="name">Gavin Morrow</p>
      <p class="role">President &amp; CEO</p>
      <p>2918 Fernhollow Dr</p>
      <p>Blacklick, OH 43871</p>
      <p>1-855-7-QVM-247</p>
      <p>gmorrow@QVM247.example</p>
    </div>
    <svg class="wave" viewBox="0 0 300 36" height="36" preserveAspectRatio="none">
      <path d="M0 14 Q100 -2 190 12 T300 6 V36 H0Z" fill="var(--grey-light)"/>
      <path d="M0 22 Q100 6 190 20 T300 14 V36 H0Z" fill="var(--green)"/>
    </svg>
  </section>

  <section class="piece card card-back">
    <div class="logo logo--white">QVM247<span class="mark"></span></div>
    <p class="web">www.QVM247.example</p>
  </section>

</body>
</html>
```